" A VELMIRA é uma empresa de consultoria de Administraçao Contratual de Obras (destacadamente no segmento de infraestrutura e construçao pesada); Elaboraçao de pleitos/reivindicaçoes ("claim") para reequilíbrio econômico-financeiro de contratos de empreendimentos; Gerenciamento de Projetos; Gestao de Empreendimentos; Fiscalizaçao; Auditoria; Gestao Empresarial; Planejamento e Controle de Obras; Análise de Riscos de Empreendimentos; Orçamentos; Suporte para elaboraçao, análise e gestao de contratos. A sede da VELMIRA fica em Brasília/DF, entretanto a atuaçao ocorre em todo o Brasil conforme demanda dos clientes e localizaçao de suas obras. "

```html
<!DOCTYPE html>
<html lang="pt-BR">
<head>
<meta charset="utf-8">
<title>VELMIRA – Envelope Saco</title>
<link href="https://fonts.googleapis.com/css2?family=Open+Sans:wght@400;600;700&family=Roboto+Condensed:wght@700&display=swap" rel="stylesheet">
<style>
  :root {
    --bg: #ececec;
    --navy: #1b4a64;
    --navy-deep: #143a50;
    --sky: #4aa3cf;
    --sky-soft: #8cc6e3;
    --paper: #ffffff;
    --paper-shade: #e9ecee;
    --ink-light: #e6f0f5;
  }
  html, body {
    margin: 0;
    padding: 0;
    width: 1200px;
    height: 1200px;
    overflow: hidden;
    background: var(--bg);
  }
  .sheet { display: block; width: 1200px; height: 1200px; }
  .section-label {
    font-family: "Roboto Condensed", sans-serif;
    font-weight: 700;
    font-size: 25px;
    fill: #ffffff;
  }
  .brand-name {
    font-family: "Roboto Condensed", sans-serif;
    font-weight: 700;
    letter-spacing: 2px;
  }
  .brand-name--back { fill: var(--paper); font-size: 30px; }
  .brand-name--front { fill: var(--navy); font-size: 66px; letter-spacing: 4px; }
  .contact-line {
    font-family: "Open Sans", sans-serif;
    font-size: 11px;
    fill: var(--ink-light);
  }
  .contact-line--strong { font-weight: 600; }
  .icon-box { fill: var(--sky-soft); }
  .icon-glyph { fill: var(--navy); }
  .icon-stroke { fill: none; stroke: var(--navy); stroke-width: 1.2; }
  .address {
    font-family: "Open Sans", sans-serif;
    font-size: 11px;
    fill: var(--ink-light);
    text-anchor: middle;
  }
  .address-title { font-weight: 700; }
  .web-address {
    font-family: "Open Sans", sans-serif;
    font-weight: 700;
    font-size: 13px;
    letter-spacing: 4px;
    fill: var(--paper);
    text-anchor: middle;
  }
</style>
</head>
<body>
<svg class="sheet" viewBox="0 0 1200 1200" xmlns="http://www.w3.org/2000/svg">
  <defs>
    <linearGradient id="frontPaper" x1="0" y1="0" x2="1" y2="1">
      <stop offset="0" stop-color="var(--paper)"/>
      <stop offset="1" stop-color="var(--paper-shade)"/>
    </linearGradient>
    <linearGradient id="backPanel" x1="0" y1="0" x2="0" y2="1">
      <stop offset="0" stop-color="#1d4f6a"/>
      <stop offset="1" stop-color="var(--navy-deep)"/>
    </linearGradient>
    <linearGradient id="backGlow" x1="0" y1="0" x2="0" y2="1">
      <stop offset="0" stop-color="#ffffff" stop-opacity="0"/>
      <stop offset="0.5" stop-color="#ffffff" stop-opacity="0.05"/>
      <stop offset="1" stop-color="#ffffff" stop-opacity="0"/>
    </linearGradient>
  </defs>

  <!-- Section label -->
  <g class="section-tag">
    <polygon points="0,36 430,36 405,84 0,84" fill="var(--navy)"/>
    <polygon points="440,36 470,36 445,84 415,84" fill="var(--sky)"/>
    <polygon points="0,84 400,84 396,90 0,90" fill="var(--sky)"/>
    <text class="section-label" x="140" y="70">ENVELOPE SACO</text>
  </g>

  <!-- Envelope back -->
  <g class="envelope-back">
    <polygon class="side-flap" points="108,350 140,322 140,1090 108,1062" fill="var(--navy)"/>
    <rect x="117" y="360" width="4" height="690" fill="var(--sky-soft)"/>
    <rect x="126" y="345" width="5" height="720" fill="var(--sky)"/>
    <path class="top-flap" d="M140,350 C150,312 190,300 250,300 L629,300 L629,360 L140,360 Z" fill="var(--navy)"/>
    <rect class="back-body" x="140" y="348" width="489" height="744" fill="url(#backPanel)"/>
    <g class="back-texture" role="img" aria-label="Faixas decorativas suaves em tons de azul">
      <rect x="140" y="600" width="489" height="360" fill="url(#backGlow)"/>
    </g>
    <rect class="bottom-flap" x="140" y="1082" width="489" height="10" fill="var(--navy-deep)"/>

    <text class="brand-name brand-name--back" x="372" y="418" text-anchor="middle">VELMIRA</text>

    <g class="contact-list">
      <g class="icon icon-phone">
        <rect class="icon-box" x="130" y="906" width="13" height="13"/>
        <path class="icon-glyph" d="M133.5,908.5 l2,0 l1,2.5 l-1.2,1 a6,6 0 0 0 2.7,2.7 l1,-1.2 l2.5,1 l0,2 a1,1 0 0 1 -1,1 a8,8 0 0 1 -8,-8 a1,1 0 0 1 1,-1 z"/>
      </g>
      <text class="contact-line contact-line--strong" x="150" y="916">(61) 3555.0142 | (61) 3555.0187</text>
      <g class="icon icon-mail">
        <rect class="icon-box" x="130" y="933" width="13" height="13"/>
        <rect class="icon-stroke" x="132.5" y="936.5" width="8" height="6"/>
        <path class="icon-stroke" d="M132.5,936.5 l4,3.2 l4,-3.2"/>
      </g>
      <text class="contact-line" x="150" y="943">contato@velmira.com.br</text>
      <rect class="icon-box" x="130" y="960" width="13" height="13"/>
      <text class="contact-line" x="150" y="970">/velmira</text>
      <rect class="icon-box" x="130" y="986" width="13" height="13"/>
      <text class="contact-line" x="150" y="996">@velmira</text>
    </g>

    <g class="postal-address">
      <text class="address address-title" x="370" y="1032">Endereço:</text>
      <text class="address" x="370" y="1047">Rua das Palmeiras, 2040 | Centro | Cidade/UF</text>
      <text class="address" x="370" y="1062">Cep: 70040-120</text>
    </g>
    <rect x="290" y="1070" width="190" height="6" fill="var(--sky)"/>
  </g>

  <!-- Envelope front -->
  <g class="envelope-front">
    <path d="M629,300 L1055,300 C1080,300 1092,318 1092,345 L1092,1092 L629,1092 Z" fill="url(#frontPaper)"/>
    <text class="brand-name brand-name--front" x="860" y="766" text-anchor="middle">VELMIRA</text>

    <rect x="629" y="1020" width="463" height="3" fill="var(--sky)"/>
    <rect x="629" y="1027" width="463" height="24" fill="var(--navy)"/>
    <text class="web-address" x="860" y="1044">www.velmira.com.br</text>
    <rect x="629" y="1055" width="463" height="3" fill="var(--sky)"/>
    <rect x="629" y="1062" width="463" height="2" fill="var(--navy)"/>
  </g>
</svg>
</body>
</html>
```